Vantage Sport And Fitness- Rates

I am opening up a new Gym/Training Facility. The Name of my New gym is Vantage Sports And Fitness. I am wanting to design a card that captures Membership Pricing/Personal Training Pricing. I will Upload the Logo. My colors are Red/Black/Silver. I really want there pricing card to "POP". IT needs to be very Professional and Clean. I will be placing these cards on a 5'7 . I would like these item on the card:
Name of Company: Vantage Sports And Fitness
Address:
2817 Larkmoor Commerce Dr.
Suite 214 Chantilly, VA 20153
Phone #: 703-555-0187
website: www.vantagesnf-example.com
Membership Rates:
$99/Month
$49 Heroes Rate
Family Plan:
2 People $149
3 People $199
4 People $299
Personal Training Rates:
1 session $102
5 sessions $490
10 sessions $940
20 sessions $1,800
40 sessions $3,400
Please be creative

```html
<!DOCTYPE html>
<html lang="en">
<head>
<meta charset="utf-8">
<title>Vantage Sports And Fitness – Rates</title>
<link rel="stylesheet" href="https://fonts.googleapis.com/css2?family=Oswald:wght@300;400;500;700&display=swap">
<style>
  :root {
    --red: #d5232b;
    --red-deep: #b8161e;
    --dark: #2a2a2c;
    --silver: #d4d4d6;
    --silver-light: #e4e4e6;
    --white: #ffffff;
    --backdrop: #6a6a6a;
  }
  * { box-sizing: border-box; margin: 0; padding: 0; }
  html, body { width: 1200px; height: 1200px; overflow: hidden; }
  body { background: var(--backdrop); font-family: "Oswald", sans-serif; }

  .card-stage { position: absolute; left: 186px; top: 20px; width: 828px; height: 1160px; }
  .rate-card {
    position: absolute; left: 0; top: 0; width: 885px; height: 1240px;
    transform: scale(0.9355); transform-origin: 0 0;
    background: var(--silver); overflow: hidden;
  }
  .card-shapes { position: absolute; inset: 0; width: 885px; height: 1240px; }

  .abs { position: absolute; }

  .brand-box {
    left: 35px; top: 38px; width: 445px; height: 147px; background: var(--white);
    box-shadow: 4px 4px 0 var(--red);
    display: flex; align-items: center; justify-content: center;
  }
  .brand-name {
    color: var(--dark); font-family: "Oswald", sans-serif; font-weight: 500;
    font-size: 40px; line-height: 1.1; text-align: center;
  }
  .brand-name span { display: block; }

  .heading-kicker { left: 32px; top: 212px; font-size: 44px; font-weight: 400; color: var(--red); line-height: 1; }
  .heading-main { left: 30px; top: 248px; font-size: 104px; font-weight: 700; color: var(--dark); line-height: 1; letter-spacing: -1px; }

  .price-disc {
    width: 134px; height: 134px; border-radius: 50%; color: var(--white);
    display: flex; align-items: center; justify-content: center;
    font-size: 56px; font-weight: 700;
  }
  .price-disc.red { background: var(--red); }
  .price-disc.dark { background: var(--dark); }

  .label { font-size: 38px; font-weight: 400; line-height: 1; text-align: center; width: 240px; }
  .label.dark, .amount.dark { color: var(--dark); }
  .label.red, .amount.red { color: var(--red); }

  .rule { height: 2px; background: #555; }

  .section-title { font-size: 46px; line-height: 1; font-weight: 400; white-space: nowrap; }
  .section-title .red { color: var(--red); }
  .section-title .dark { color: var(--dark); }
  .section-title .bold { font-weight: 500; }

  .badge {
    border-radius: 50%; color: var(--white); text-align: center;
    display: flex; flex-direction: column; align-items: center; justify-content: center;
    line-height: 1;
  }
  .badge.red { background: var(--red); border: 4px solid var(--red); box-shadow: inset 0 0 0 3px var(--white); }
  .badge.dark { background: var(--dark); border: 4px solid var(--dark); box-shadow: inset 0 0 0 3px var(--white); }
  .family-badge { width: 116px; height: 116px; }
  .family-badge .num { font-size: 34px; font-weight: 500; }
  .family-badge .unit { font-size: 24px; font-weight: 400; margin-top: 2px; }
  .session-badge { width: 94px; height: 94px; }
  .session-badge .num { font-size: 19px; font-weight: 400; }
  .session-badge .unit { font-size: 19px; font-weight: 400; margin-top: 3px; }

  .amount { font-size: 32px; font-weight: 500; text-align: center; width: 140px; line-height: 1; }
  .amount.small { font-size: 30px; width: 120px; }

  .address { left: 280px; top: 1098px; width: 500px; text-align: center; color: var(--dark); font-size: 26px; line-height: 31px; font-weight: 400; font-style: normal; }
  .contact-row { left: 305px; top: 1170px; display: flex; align-items: center; gap: 10px; color: var(--dark); font-size: 25px; white-space: nowrap; }
  .contact-icon {
    width: 38px; height: 38px; border-radius: 50%; background: var(--dark); color: var(--white);
    display: flex; align-items: center; justify-content: center; font-size: 22px; flex: none;
  }
  .contact-row .gap { width: 6px; }
</style>
</head>
<body>
<main class="card-stage">
  <section class="rate-card">
    <svg class="card-shapes" viewBox="0 0 885 1240" aria-hidden="true">
      <polygon points="290,0 885,0 885,1240 780,1240 780,1010" fill="var(--red)"/>
      <polygon points="780,1060 885,1240 700,1240" fill="var(--silver)"/>
      <polygon points="0,770 0,1240 230,1240" fill="var(--red)"/>
      <polygon points="318,108 793,108 793,1075 782,1085" fill="var(--dark)"/>
      <polygon points="40,785 40,1212 252,1212" fill="var(--dark)"/>
    </svg>

    <svg class="card-shapes" viewBox="0 0 885 1240" role="img" aria-label="Photo of a man lifting dumbbells on a weight bench in the gym">
      <defs>
        <linearGradient id="gymShot" x1="0" y1="0" x2="1" y2="1">
          <stop offset="0" stop-color="#e9e7e6"/>
          <stop offset="0.5" stop-color="#8a7f7c"/>
          <stop offset="1" stop-color="#3a3132"/>
        </linearGradient>
      </defs>
      <polygon points="330,122 775,122 775,1080" fill="url(#gymShot)"/>
    </svg>

    <svg class="card-shapes" viewBox="0 0 885 1240" role="img" aria-label="Photo of a woman training in a red sports top">
      <defs>
        <linearGradient id="trainerShot" x1="0" y1="0" x2="0" y2="1">
          <stop offset="0" stop-color="#4a4547"/>
          <stop offset="0.6" stop-color="#9a3a3c"/>
          <stop offset="1" stop-color="#2c2a2b"/>
        </linearGradient>
      </defs>
      <polygon points="50,800 50,1200 240,1200" fill="url(#trainerShot)"/>
    </svg>

    <svg class="card-shapes" viewBox="0 0 885 1240" aria-hidden="true">
      <circle cx="90" cy="432" r="60" fill="var(--dark)"/>
      <circle cx="365" cy="432" r="60" fill="var(--red)"/>
      <circle cx="143" cy="432" r="73" fill="var(--silver)"/>
      <circle cx="310" cy="432" r="73" fill="var(--silver)"/>
    </svg>

    <header class="abs brand-box">
      <p class="brand-name"><span>VANTAGE</span><span>SPORTS AND FITNESS</span></p>
    </header>

    <h1 class="abs heading-kicker">MEMBERSHIP</h1>
    <h2 class="abs heading-main">RATES</h2>

    <div class="abs price-disc red" style="left:76px; top:365px;">$99</div>
    <div class="abs price-disc dark" style="left:243px; top:365px;">$49</div>
    <p class="abs label dark" style="left:23px; top:512px;">MONTH</p>
    <p class="abs label red" style="left:190px; top:512px;">HEROES RATE</p>

    <div class="abs rule" style="left:15px; top:572px; width:495px;"></div>

    <h3 class="abs section-title" style="left:28px; top:598px;"><span class="red">FAMILY</span> <span class="dark bold">PLAN</span></h3>

    <div class="abs badge red family-badge" style="left:84px; top:655px;"><span class="num">02</span><span class="unit">PEOPLE</span></div>
    <div class="abs badge dark family-badge" style="left:248px; top:655px;"><span class="num">03</span><span class="unit">PEOPLE</span></div>
    <div class="abs badge red family-badge" style="left:413px; top:655px;"><span class="num">04</span><span class="unit">PEOPLE</span></div>
    <p class="abs amount dark" style="left:72px; top:779px;">$149</p>
    <p class="abs amount red" style="left:236px; top:779px;">$199</p>
    <p class="abs amount dark" style="left:401px; top:779px;">$299</p>

    <div class="abs rule" style="left:95px; top:837px; width:540px;"></div>

    <h3 class="abs section-title" style="left:150px; top:860px;"><span class="dark">PERSONAL</span> <span class="red bold">TRAINING RATES</span></h3>

    <div class="abs badge red session-badge" style="left:175px; top:918px;"><span class="num">01</span><span class="unit">SESSION</span></div>
    <div class="abs badge dark session-badge" style="left:279px; top:918px;"><span class="num">05</span><span class="unit">SESSIONS</span></div>
    <div class="abs badge red session-badge" style="left:384px; top:918px;"><span class="num">10</span><span class="unit">SESSIONS</span></div>
    <div class="abs badge dark session-badge" style="left:488px; top:918px;"><span class="num">20</span><span class="unit">SESSIONS</span></div>
    <div class="abs badge red session-badge" style="left:592px; top:918px;"><span class="num">40</span><span class="unit">SESSIONS</span></div>
    <p class="abs amount small dark" style="left:162px; top:1023px;">$102</p>
    <p class="abs amount small red" style="left:266px; top:1023px;">$490</p>
    <p class="abs amount small dark" style="left:371px; top:1023px;">$940</p>
    <p class="abs amount small red" style="left:475px; top:1023px;">$1,800</p>
    <p class="abs amount small dark" style="left:579px; top:1023px;">$3,400</p>

    <address class="abs address">
      Address: 2817 Larkmoor Commerce Dr.<br>
      Suite 214 Chantilly, VA 20153
    </address>
    <p class="abs contact-row">
      <span class="contact-icon">P</span><span>703-555-0187</span>
      <span class="gap"></span>
      <span class="contact-icon">W</span><span>www.vantagesnf-example.com</span>
    </p>
  </section>
</main>
</body>
</html>
```